Real Estate Company Website

We are working with ZP Real Estate and building a new website for them.
Some sites to use for content/competitors and inspiration:
https://doranpeltz.vq.com
https://www.dwellorix.com
https://www.mansard47.com
https://delphinetorsby.com
https://ottiliefrenz.com
https://simonpellor.com
https://noraquistelgroup.com
Thank you for taking the time to consider designing a website for us. We are web developers based in Stockton, CA, USA. Most of our projects go through the same process. Understanding this process may help you win a project with us. We custom-code all of our websites in-house. We don’t have any requirements as to what tools you use for your design, but we prefer Figma files. For any design that we label as four stars, we send it to the client for review. The client picks the final design they want us to use. Once we complete this process, we will continue to show additional clients all the four-star sites and purchase them later. Your designs will have multiple chances to sell. For better chances of success, we ask that you follow these guidelines.
IMAGES:
If you use any images or icons in the design, we ask that you have a link to the asset so we can purchase the image/icon. Most of the designs we submit do not have the customer’s images on them unless they have some great images. Be creative; show us the feeling you are trying to portray with your image choices. Use any royalty-free site you choose. We subscribe to Vexlo and mainly use their images, but we can purchase images outside of Vexlo. PLEASE NOTE: we will not submit designs to clients with watermarks on the images.
FONTS:
We ask that you identify the fonts used in the design. This can be done in a message if you want. We typically use Nubrik Fonts and Vexlo Fonts.
CONTENT:
We're always open to different content and ideas. We often submit designs with stock images so the client can see our vision. We typically take pictures after the website launch to use their images with our vision. Lorem Ipsum is fine for paragraphs, but we ask that you write the headers in correct English. We want to be able to show the vision and identify the sections of the website.
INSPIRATION:
We typically add a couple of links in the brief of websites we like to help you get started in your design.
REVISIONS:
We do not often ask for revisions of the designs unless we see something in the design that may not appeal to the client. If there are slight changes that we want to make, we do that in the development process.
FEEDBACK:
We rarely give feedback on designs during the design process. We are working on many website projects and do not have the time to provide feedback. We usually respond if your request is well thought out and asks specific questions, but a note asking “feedback, please” usually goes unanswered.

```html
<!DOCTYPE html>
<html lang="en">
<head>
<meta charset="utf-8">
<title>ZP Real Estate</title>
<link href="https://fonts.googleapis.com/css2?family=Playfair+Display:wght@400;500;600;700&display=swap" rel="stylesheet">
<style>
:root{
  --teal:#1a5d70;
  --teal-dark:#174f60;
  --ink:#111;
  --muted:#6b6b6b;
  --gray-band:#e6e6e6;
  --line:#d5d5d5;
  --footer:#1b1b1b;
  --white:#fff;
}
*{box-sizing:border-box;margin:0;padding:0}
html,body{width:1200px;height:4144px;overflow:hidden}
body{position:relative;background:var(--white);font-family:"Playfair Display",Georgia,serif;color:var(--ink)}
.abs{position:absolute}
.center{left:0;width:1200px;text-align:center}

/* hero */
.hero{left:0;top:0;width:1200px;height:690px;background:linear-gradient(180deg,#5a6878 0%,#4a5562 45%,#6b5a44 80%,#3f4a3c 100%)}
.brand{left:101px;top:22px;color:var(--white);font-size:20px;font-weight:700;letter-spacing:.5px;display:flex;align-items:center;gap:10px}
.brand .mark{width:18px;height:18px;background:var(--teal)}
.nav{top:44px;left:391px;display:flex;align-items:center;gap:0;color:var(--white);font-size:15px;font-weight:600}
.nav span{padding:6px 11px;margin-right:13px}
.nav .active{background:var(--teal)}
.burger{display:inline-flex;flex-direction:column;gap:5px;margin-left:6px}
.burger i{display:block;width:26px;height:3px;background:var(--white)}
.welcome{top:228px;color:var(--white);font-size:35px;font-weight:400;letter-spacing:.5px}
.hero-title{top:270px;color:var(--white);font-size:64px;font-weight:700}
.tabs{top:364px;left:265px;display:flex;gap:0;color:var(--white);font-size:15px;font-weight:600}
.tabs span{padding:3px 7px;margin-right:17px}
.tabs .active{background:var(--teal)}
.search{left:265px;top:404px;width:673px;height:74px;background:var(--white);border-radius:37px;display:flex;align-items:center;padding-left:33px;font-size:16px;font-weight:600}
.search .go{position:absolute;right:9px;top:9px;width:56px;height:56px;border-radius:50%;background:var(--teal);display:flex;align-items:center;justify-content:center}

/* section heading */
.kicker{font-size:14px;font-weight:700;color:var(--teal);letter-spacing:2px}
.h2{font-size:32px;font-weight:500;text-transform:uppercase}

/* cards */
.card{top:910px;width:311px;height:406px;border:2px solid var(--line);border-radius:12px;overflow:hidden;background:var(--white);text-align:center}
.card .photo{height:228px}
.card .type{margin-top:15px;font-size:21px;font-weight:600;color:var(--teal)}
.card .addr{margin-top:6px;font-size:16px;line-height:26px;padding:0 40px}
.card .price{margin:12px 20px 0;display:flex;align-items:center;gap:10px;font-size:17px;font-weight:700}
.card .price:before,.card .price:after{content:"";flex:1;height:1px;background:#999}
.card .specs{margin-top:10px;font-size:13px;font-weight:600;color:var(--teal)}
.arrow{width:36px;height:36px;border-radius:50%;background:var(--white);box-shadow:0 2px 6px rgba(0,0,0,.25);display:flex;align-items:center;justify-content:center}

/* about */
.about-band{left:0;top:1383px;width:1200px;height:716px;background:var(--gray-band)}
.about-photo{left:101px;top:1475px;width:565px;height:533px;background:linear-gradient(160deg,#5b5f63 0%,#8a7a66 45%,#6f8a5a 100%)}
.about-card{left:568px;top:1533px;width:534px;height:417px;background:var(--white);padding:44px 38px 0 29px}
.about-card .h2{font-size:30px;margin-top:16px}
.about-card p{margin-top:24px;font-size:14px;line-height:26px;color:var(--muted)}
.btn{display:inline-block;background:var(--teal);color:var(--white);font-weight:700;font-size:20px}
.about-card .btn{margin-top:22px;width:173px;height:51px;line-height:51px;text-align:center}

/* markets */
.lead{font-size:15px;line-height:25px;color:var(--muted)}
.stat{top:2439px;width:237px;height:123px;border:2px solid var(--line);border-radius:14px;text-align:center}
.stat b{display:block;margin-top:14px;font-size:40px;font-weight:500}
.stat small{display:block;margin-top:6px;font-size:16px}
.stat.hl{background:var(--teal);border-color:var(--teal);color:var(--white)}
.video{left:101px;top:2637px;width:998px;height:563px;border-radius:42px;background:linear-gradient(90deg,#8c6a55 0%,#cfcac2 35%,#e6e4e0 60%,#b9b4ab 100%)}
.play{left:574px;top:2892px;width:53px;height:53px;border-radius:50%;background:var(--teal);display:flex;align-items:center;justify-content:center}

/* newsletter */
.field{top:3555px;height:54px;border:1.5px solid var(--line);border-radius:4px;padding:0 16px;font-size:14px;line-height:51px}
.submit{left:898px;top:3555px;width:204px;height:54px;line-height:54px;text-align:center;border-radius:4px;font-size:19px}

/* footer */
.footer{left:0;top:3711px;width:1200px;height:375px;background:var(--footer);color:var(--white)}
.foot-brand{left:103px;top:3890px;font-size:42px;font-weight:700;color:var(--white);letter-spacing:1px;display:flex;align-items:center;gap:14px}
.foot-brand .mark{width:30px;height:30px;background:var(--teal)}
.fcol{top:3820px;color:var(--white)}
.fcol h4{font-size:20px;font-weight:600;margin-bottom:20px}
.fcol li{list-style:none;font-size:17px;line-height:32px}
.contact li{display:flex;gap:12px;font-size:15px;line-height:24px;margin-bottom:14px}
.contact svg{flex:none;margin-top:4px}
.copy{left:0;top:4086px;width:1200px;height:58px;background:var(--teal);color:var(--white);font-size:16px;font-weight:700;text-align:center;line-height:58px}
.copy small{position:absolute;right:18px;font-size:12px;font-weight:400}
</style>
</head>
<body>

<header>
  <div class="abs hero" role="img" aria-label="Photo of modern apartment buildings under a dusk sky"></div>
  <div class="abs brand"><span class="mark"></span>ZP Real Estate</div>
  <nav class="abs nav">
    <span class="active">HOME</span><span>ABOUT ME</span><span>SEARCH PROPERTIES</span><span>BLOG</span><span>(555)010-2468</span><span style="margin-right:0">MENU</span>
    <span class="burger"><i></i><i></i><i></i></span>
  </nav>
  <div class="abs center welcome">WELCOME TO</div>
  <h1 class="abs center hero-title">ZP REAL ESTATE</h1>
  <div class="abs tabs"><span class="active">BUY</span><span>RENT</span><span>SELL</span><span>PRE-APPROVAL</span><span>AGENTS</span><span>JUST SOLD</span><span>HOME VALUE</span></div>
  <div class="abs search">Search
    <span class="go"><svg width="26" height="26" viewBox="0 0 24 24" fill="none" stroke="#fff" stroke-width="3"><circle cx="10" cy="10" r="6.5"/><path d="M15 15l6 6" stroke-linecap="round"/></svg></span>
  </div>
</header>

<section class="featured">
  <div class="abs center kicker" style="top:788px">ZP REAL ESTATE</div>
  <h2 class="abs center h2" style="top:830px">Featured Properties</h2>

  <article class="abs card" style="left:100px">
    <div class="photo" role="img" aria-label="Photo of an agent presenting a house model to a client" style="background:linear-gradient(135deg,#d9d9d9,#8a8f96 60%,#3d4a5a)"></div>
    <div class="type">AGENTS</div>
    <div class="addr">3120 Lorem ipsum dolor sit adipiscing 89121</div>
    <div class="price">Price: $320,000</div>
    <div class="specs">3,530 Sq.fit - 4 Bed - 3 Bath - 3 Garage</div>
  </article>
  <article class="abs card" style="left:444px">
    <div class="photo" role="img" aria-label="Photo of a couple receiving keys in a bright kitchen" style="background:linear-gradient(135deg,#f1f1f1,#c9ccd0 55%,#6d4a6a)"></div>
    <div class="type">BUY</div>
    <div class="addr">3120 Lorem ipsum dolor sit adipiscing 89121</div>
    <div class="price">Price: $320,000</div>
    <div class="specs">3,530 Sq.fit - 4 Bed - 3 Bath - 3 Garage</div>
  </article>
  <article class="abs card" style="left:790px">
    <div class="photo" role="img" aria-label="Photo of a suburban street lined with family homes" style="background:linear-gradient(180deg,#b9d4ec 0%,#e4ebf2 40%,#6c7a6a 70%,#8f8f8f 100%)"></div>
    <div class="type">VILLA</div>
    <div class="addr">3120 Lorem ipsum dolor sit adipiscing 89121</div>
    <div class="price">Price: $320,000</div>
    <div class="specs">3,530 Sq.fit - 4 Bed - 3 Bath - 3 Garage</div>
  </article>

  <span class="abs arrow" style="left:79px;top:1113px"><svg width="12" height="14" viewBox="0 0 12 14"><path d="M8 2L3 7l5 5" fill="none" stroke="#1a5d70" stroke-width="2"/></svg></span>
  <span class="abs arrow" style="left:1082px;top:1113px"><svg width="12" height="14" viewBox="0 0 12 14"><path d="M4 2l5 5-5 5" fill="none" stroke="#1a5d70" stroke-width="2"/></svg></span>
</section>

<section class="about">
  <div class="abs about-band"></div>
  <div class="abs about-photo" role="img" aria-label="Photo of a couple embracing in front of a modern house"></div>
  <div class="abs about-card">
    <div class="kicker">ZP REAL ESTATE</div>
    <h2 class="h2">About Us</h2>
    <p>Sed ut perspiciatis unde omnis iste natus error sit voluptatem accusantium doloremque laudantium, totam rem aperiam, eaque ipsa quae ab illo inventore veritatis et quasi architecto beatae vitae dicta sunt explicabo. Nemo enim ipsam voluptatem quia voluptas sit aspernatur aut odit aut fugit, sed quia consequuntur magni dolores eos qui ratione voluptatem sequi nesciunt.</p>
    <span class="btn">Read More</span>
  </div>
</section>

<section class="markets">
  <div class="abs center kicker" style="top:2208px">ZP REAL ESTATE</div>
  <h2 class="abs center h2" style="top:2254px">Getting to Know Real Estate Markets</h2>
  <p class="abs lead" style="left:220px;top:2316px;width:760px;text-align:center">Sed ut perspiciatis unde omnis iste natus error sit voluptatem accusantium doloremque laudantium, totam rem aperiam, eaque ipsa quae ab illo inventore veritatis et quasi architecto beatae vitae dicta sunt explicabo. Nemo enim ipsam voluptatem quia voluptas sit</p>

  <div class="abs stat" style="left:97px"><b>$100M</b><small>in Career Sales</small></div>
  <div class="abs stat hl" style="left:352px"><b>180+</b><small>Deals Closed</small></div>
  <div class="abs stat" style="left:610px"><b>2.45%</b><small>All Agents</small></div>
  <div class="abs stat" style="left:865px"><b>1800 +</b><small>Sales</small></div>

  <div class="abs video" role="img" aria-label="Video still of an agent welcoming a couple into a bright empty home"></div>
  <span class="abs play"><svg width="20" height="22" viewBox="0 0 20 22"><path d="M4 2l14 9-14 9z" fill="#fff"/></svg></span>
</section>

<section class="newsletter">
  <div class="abs center kicker" style="top:3298px">ZP REAL ESTATE</div>
  <h2 class="abs center h2" style="top:3344px;line-height:40px">Receive the Latest ZP Real Estate Market<br>Trends in Your Inbox</h2>
  <p class="abs lead" style="left:165px;top:3438px;width:870px;text-align:center;font-size:14px">Sed ut perspiciatis unde omnis iste natus error sit voluptatem accusantium doloremque laudantium, totam rem aperiam, eaque ipsa quae ab illo inventore veritatis et quasi architecto beatae vitae dicta sunt explicabo. Nemo enim ipsam voluptatem quia voluptas sit aspernatur aut odit aut fugit, sed quia consequuntur magni dolores eos qui ratione voluptatem sequi nesciunt.</p>
  <div class="abs field" style="left:98px;width:256px">Name</div>
  <div class="abs field" style="left:364px;width:255px">Email</div>
  <div class="abs field" style="left:629px;width:256px">Phone</div>
  <span class="abs btn submit">Submit Now</span>
</section>

<footer>
  <div class="abs footer"></div>
  <div class="abs foot-brand"><span class="mark"></span>ZP REAL ESTATE</div>
  <div class="abs fcol" style="left:516px">
    <h4>QUICK LINK</h4>
    <ul><li>Home</li><li>About Me</li><li>Search Properties</li><li>Blog</li></ul>
  </div>
  <div class="abs fcol contact" style="left:698px">
    <h4>CONTACT</h4>
    <ul>
      <li><svg width="12" height="16" viewBox="0 0 12 16"><path d="M6 0a6 6 0 0 0-6 6c0 4.5 6 10 6 10s6-5.5 6-10a6 6 0 0 0-6-6zm0 8.5A2.5 2.5 0 1 1 6 3.5a2.5 2.5 0 0 1 0 5z" fill="#fff"/></svg><span>Neque porro quisquam<br>qui dolorem ipsum 1250</span></li>
      <li><svg width="14" height="14" viewBox="0 0 24 24"><path d="M6.6 10.8a15.1 15.1 0 0 0 6.6 6.6l2.2-2.2c.3-.3.7-.4 1-.2 1.1.4 2.3.6 3.6.6.6 0 1 .4 1 1V20c0 .6-.4 1-1 1A17 17 0 0 1 3 4c0-.6.4-1 1-1h3.5c.6 0 1 .4 1 1 0 1.3.2 2.5.6 3.6.1.3 0 .7-.2 1z" fill="#fff"/></svg><span>+1 555 010 2468</span></li>
      <li><svg width="16" height="12" viewBox="0 0 16 12"><rect x="1" y="1" width="14" height="10" fill="none" stroke="#fff" stroke-width="1.5"/><path d="M1 1l7 6 7-6" fill="none" stroke="#fff" stroke-width="1.5"/></svg><span>zprealestate@mail.com</span></li>
    </ul>
  </div>
  <div class="abs fcol" style="left:957px">
    <h4>HELP LINK</h4>
    <ul><li>Terms&amp;condtions</li><li>Privacy Policy</li><li>About Us</li><li>Support</li></ul>
  </div>
  <div class="abs copy">© copyrights 2024 ZP Real Estate | All Rights Reserved<small>C 25</small></div>
</footer>

</body>
</html>
```